Business Card Design Project

I need the following:

Logo -
Name - Dale Prewitt
Title - Customer Experience Officer
Web - www.bvrh.net
Phone - 555-417-3068
Updates

Project Deadline Extended
Reason: I launched the project later than anticipated. I look forward to seeing your designs. Dale

Industry/Entity Type

Business

```html
<!DOCTYPE html>
<html lang="en">
<head>
<meta charset="utf-8">
<title>Bayview Relay Holdings – Business Card</title>
<link rel="stylesheet" href="https://fonts.googleapis.com/css2?family=Orbitron:wght@800&family=Saira:wght@400;500;600&display=swap">
<style>
  :root{
    --page:#f3f5f7;
    --sky-light:#e4f4fc;
    --sky-mid:#9fd3ee;
    --sky-deep:#3d86cc;
    --navy:#28377f;
    --ink:#141821;
    --link-blue:#2f7fc8;
    --silver-light:#ffffff;
    --silver-dark:#9aa6b2;
    --band:rgba(40,110,180,0.16);
  }
  *{margin:0;padding:0;box-sizing:border-box}
  html,body{width:1200px;height:900px;overflow:hidden}
  body{background:var(--page);position:relative;font-family:"Saira",sans-serif}

  .card{
    position:absolute;left:100px;top:165px;width:1000px;height:571px;
    border-radius:36px;overflow:hidden;
    box-shadow:0 18px 40px rgba(0,0,0,0.18);
  }
  .card-backdrop{
    position:absolute;inset:0;
    background:
      radial-gradient(ellipse at 25% 30%, rgba(255,255,255,0.85), transparent 55%),
      linear-gradient(110deg,var(--sky-light) 0%,var(--sky-mid) 45%,var(--sky-deep) 100%);
  }
  .info-band{
    position:absolute;left:0;right:0;top:300px;height:222px;
    background:linear-gradient(90deg,var(--band),rgba(40,110,180,0.05));
  }
  .silver-rule{
    position:absolute;left:0;right:0;height:8px;
    background:linear-gradient(180deg,var(--silver-dark),var(--silver-light) 45%,var(--silver-dark));
  }
  .silver-rule.top{top:296px}
  .silver-rule.bottom{top:518px}

  .brand-mark{
    position:absolute;left:50px;top:108px;
    display:flex;align-items:center;gap:14px;
    font-family:"Saira",sans-serif;font-weight:600;font-size:38px;color:var(--navy);
    letter-spacing:1px;
  }
  .brand-mark .dot{width:112px;height:112px;border-radius:50%;background:var(--navy)}

  .company{
    position:absolute;left:370px;top:104px;
    font-family:"Orbitron",sans-serif;font-weight:800;font-size:36px;line-height:1.02;color:var(--ink);
    text-transform:uppercase;letter-spacing:1px;
  }
  .company-url{
    position:absolute;left:370px;top:228px;width:330px;
    display:flex;align-items:center;gap:10px;
    font-size:16px;font-weight:500;color:var(--link-blue);
  }
  .company-url::before,.company-url::after{content:"";flex:1;height:2px;background:var(--link-blue)}

  .person{position:absolute;left:52px;top:318px}
  .person-name{font-size:40px;font-weight:500;color:var(--navy);line-height:1.1;letter-spacing:1px}
  .person-title{font-size:21px;color:var(--ink);letter-spacing:0.5px}

  .contact{position:absolute;left:52px;display:flex;align-items:center;gap:14px;
    font-size:36px;font-weight:500;color:var(--ink);letter-spacing:1px}
  .contact.phone{top:412px}
  .contact.web{top:468px}
  .contact svg{width:38px;height:38px}
</style>
</head>
<body>
  <div class="card">
    <div class="card-backdrop" role="img" aria-label="Soft blue background with a fine perspective grid of light lines"></div>
    <div class="info-band"></div>
    <div class="silver-rule top"></div>
    <div class="silver-rule bottom"></div>

    <div class="brand-mark"><span class="dot"></span>BVRH</div>

    <div class="company">Bayview<br>Relay<br>Holdings</div>
    <div class="company-url">www.bvrh.net</div>

    <div class="person">
      <div class="person-name">Dale Prewitt</div>
      <div class="person-title">Customer Experience Officer</div>
    </div>

    <div class="contact phone">
      <svg viewBox="0 0 40 40" aria-hidden="true">
        <circle cx="20" cy="20" r="17" fill="none" stroke="#28377f" stroke-width="3"/>
        <path d="M14 11c-2 1-3 3-2 6 2 6 6 10 12 12 3 1 5 0 6-2l-4-4-3 2c-3-1-6-4-7-7l2-3z" fill="#28377f"/>
      </svg>
      <span>555-417-3068</span>
    </div>
    <div class="contact web">
      <svg viewBox="0 0 40 40" aria-hidden="true">
        <circle cx="20" cy="20" r="17" fill="#28377f"/>
        <g fill="none" stroke="#fff" stroke-width="1.6">
          <circle cx="20" cy="20" r="10"/>
          <ellipse cx="20" cy="20" rx="4.5" ry="10"/>
          <line x1="10" y1="20" x2="30" y2="20"/>
          <line x1="12" y1="14" x2="28" y2="14"/>
          <line x1="12" y1="26" x2="28" y2="26"/>
        </g>
      </svg>
      <span>www.bvrh.net</span>
    </div>
  </div>
</body>
</html>
```